Kestrel Vale - Multifamily Development

Kestrel Vale is a Luxury Multifamily Development project located in Orange, NJ. This project will be completed in three phases with the first phase about 75% complete. Each phase will have a different name as follows
ALDER Kestrel Vale
WILLOW Kestrel Vale
JUNIPERS Kestrel Vale
We are going to install a banner on the side of the first building which will act as advertising for all buildings. We will eventually need advertising that will be in the windows as well as marketing materials . We want the marketing for this project to be similar for all three phases. At the moment, we are starting with this first simple banner. Attached is a rough idea of the look as well as our color palette. If you feel the color palette is a little too monochrome, feel free to propose an accent color. You can also visit our website to see more info on our company as well as the project. www.tarnvx.com Finally, if you need AI files (ie. for the logo), we can send to you. Thanks..

```html
<!DOCTYPE html>
<html lang="en">
<head>
<meta charset="utf-8">
<title>ALDER Kestrel Vale – Banner</title>
<link rel="stylesheet" href="https://fonts.googleapis.com/css2?family=Montserrat:wght@400;500;600;800&display=swap">
<style>
  :root {
    --page-bg: #e6e6e6;
    --white: #ffffff;
    --ink: #322d30;
    --accent-blue: #4a6a9e;
    --panel-light: #414e6c;
    --panel-dark: #2e384e;
  }
  * { margin: 0; padding: 0; box-sizing: border-box; }
  html, body {
    width: 849px; height: 1200px; overflow: hidden;
    background: var(--page-bg);
    font-family: "Montserrat", sans-serif;
  }
  .banner {
    position: absolute; left: 292px; top: 62px;
    width: 260px; height: 1075px;
    background: var(--white);
  }
  .brand {
    position: absolute; left: 0; top: 0; width: 260px; height: 186px;
    display: flex; flex-direction: column; align-items: center; justify-content: center;
    color: var(--ink); font-weight: 600; padding-top: 20px;
  }
  .brand-name { font-size: 62px; line-height: 1; letter-spacing: -1px; }
  .brand-sub { font-size: 15px; letter-spacing: 7px; margin-top: 8px; padding-left: 7px; }
  .feature {
    position: absolute; left: 0; top: 186px; width: 260px; height: 822px;
    background: var(--accent-blue);
    color: var(--white);
  }
  .feature svg { position: absolute; inset: 0; }
  .project-name {
    position: absolute; left: 50px; width: 180px; top: 20px;
    text-align: center; font-size: 24px; line-height: 37px; font-weight: 400;
  }
  .phone {
    position: absolute; left: 109px; width: 40px; top: 220px;
    display: flex; flex-direction: column; align-items: center;
    font-size: 36px; font-weight: 800; line-height: 39px;
  }
  .tagline {
    position: absolute; left: 21px; width: 200px; top: 691px;
    text-align: center; font-size: 27px; line-height: 41px; font-weight: 400;
  }
  .web {
    position: absolute; left: 0; bottom: 0; width: 260px; height: 67px;
    display: flex; align-items: center; justify-content: center;
    font-size: 29px; color: var(--ink); font-weight: 400;
  }
</style>
</head>
<body>
  <div class="banner">
    <header class="brand">
      <span class="brand-name">TARN</span>
      <span class="brand-sub">PROPERTIES</span>
    </header>
    <section class="feature">
      <svg width="260" height="822" viewBox="0 0 260 822" aria-hidden="true">
        <defs>
          <linearGradient id="panelFill" x1="0" x2="1" y1="0" y2="0">
            <stop offset="0" stop-color="var(--panel-light)"/>
            <stop offset="1" stop-color="var(--panel-dark)"/>
          </linearGradient>
          <filter id="panelShadow" x="-10%" y="-5%" width="120%" height="110%">
            <feDropShadow dx="0" dy="0" stdDeviation="3" flood-color="#000" flood-opacity="0.45"/>
          </filter>
        </defs>
        <polygon points="50,0 260,0 232,822 2,822" fill="url(#panelFill)" filter="url(#panelShadow)"/>
      </svg>
      <h1 class="project-name">ALDER<br>KESTREL<br>VALE</h1>
      <div class="phone" aria-label="973-555-0148">
        <span>9</span><span>7</span><span>3</span><span>-</span><span>5</span><span>5</span><span>5</span><span>-</span><span>0</span><span>1</span><span>4</span><span>8</span>
      </div>
      <p class="tagline">LUXURY<br>APARTMENT<br>RENTALS</p>
    </section>
    <footer class="web">tarnvx.com</footer>
  </div>
</body>
</html>
```